BrivoLane Ute.

I want the full logo on one side. And the other side the card if right Ralf the logo the left half orange like the car in the logo color with Danielle R Morrow
Founder and CEO
Email symbol then dmorrow@brivolaneute.com
Www symbol. Then Brivolaneute.com
Phone symbol then 413-926-BRIV
The very bottom would like Brivo Lane Ute is a division of Harmond Vistas. LLC

```html
<!DOCTYPE html>
<html lang="en">
<head>
<meta charset="utf-8">
<title>Brivo Lane Ute – Business Card</title>
<link rel="stylesheet" href="https://fonts.googleapis.com/css2?family=Raleway:wght@400;500;600&display=swap">
<style>
  :root {
    --bg: #e9e9ea;
    --card: #ffffff;
    --orange: #f0901f;
    --orange-deep: #e27f12;
    --accent-red: #c8372d;
    --ink: #2a2a2a;
    --white: #ffffff;
    --shadow: 0 6px 18px rgba(0,0,0,0.12);
  }
  * { box-sizing: border-box; margin: 0; padding: 0; }
  html, body {
    width: 1200px; height: 870px; overflow: hidden;
    background: var(--bg);
    font-family: "Raleway", Arial, sans-serif;
  }
  .stage {
    width: 1200px; height: 870px;
    display: flex; align-items: center; justify-content: center; gap: 44px;
  }
  .card {
    position: relative;
    width: 540px; height: 310px;
    background: var(--card);
    border-radius: 14px;
    box-shadow: var(--shadow);
    overflow: hidden;
  }
  .brand {
    display: flex; align-items: center; justify-content: center; gap: 10px;
    color: var(--ink);
    font-weight: 600;
    letter-spacing: 0.06em;
    text-transform: uppercase;
    white-space: nowrap;
  }
  .brand-dot {
    width: 16px; height: 16px; border-radius: 50%;
    background: var(--orange);
    flex: none;
  }
  /* front */
  .card-front .brand-area {
    position: absolute; left: 0; top: 0; width: 50%; height: 100%;
    display: flex; align-items: center; justify-content: center;
  }
  .card-front .brand { font-size: 22px; }
  .contact-panel {
    position: absolute; right: 0; top: 0; width: 50%; height: 100%;
    background: linear-gradient(160deg, var(--orange) 0%, var(--orange-deep) 100%);
    border-left: 3px solid var(--accent-red);
    padding: 40px 26px 22px 30px;
    color: var(--white);
  }
  .notch {
    position: absolute; left: -3px; top: 44px;
    width: 0; height: 0;
    border-top: 8px solid transparent;
    border-bottom: 8px solid transparent;
    border-left: 9px solid var(--accent-red);
  }
  .person-name {
    color: var(--accent-red);
    font-size: 15px; font-weight: 500;
    letter-spacing: 0.04em; text-transform: uppercase;
  }
  .person-role { font-size: 12px; margin-top: 4px; }
  .contact-list { list-style: none; margin-top: 26px; }
  .contact-list li {
    display: flex; align-items: center; gap: 8px;
    font-size: 11.5px; margin-bottom: 8px;
  }
  .contact-icon {
    width: 16px; height: 16px; flex: none;
  }
  .division {
    position: absolute; left: 30px; bottom: 22px;
    font-size: 9px; letter-spacing: 0.06em; text-transform: uppercase;
  }
  /* back */
  .card-back { display: flex; align-items: center; justify-content: center; }
  .card-back .brand { font-size: 30px; }
</style>
</head>
<body>
<main class="stage">
  <section class="card card-front" aria-label="Card front">
    <div class="brand-area">
      <div class="brand"><span class="brand-dot"></span>Brivo Lane Ute</div>
    </div>
    <div class="contact-panel">
      <span class="notch"></span>
      <h1 class="person-name">Danielle R Morrow</h1>
      <p class="person-role">Founder and CEO</p>
      <ul class="contact-list">
        <li>
          <svg class="contact-icon" viewBox="0 0 16 16" aria-hidden="true">
            <circle cx="8" cy="8" r="8" fill="#c8372d"/>
            <path d="M5.2 4.2l1.4-.3.8 1.9-.9.7a5 5 0 0 0 2.9 2.9l.7-.9 1.9.8-.3 1.4c-3.6.3-6.8-2.9-6.5-6.5z" fill="#fff"/>
          </svg>
          413-926-BRIV
        </li>
        <li>
          <svg class="contact-icon" viewBox="0 0 16 16" aria-hidden="true">
            <circle cx="8" cy="8" r="8" fill="#c8372d"/>
            <rect x="4" y="5" width="8" height="6" rx="0.8" fill="none" stroke="#fff" stroke-width="1"/>
            <path d="M4.3 5.4L8 8.4l3.7-3" fill="none" stroke="#fff" stroke-width="1"/>
          </svg>
          dmorrow@brivolaneute.com
        </li>
        <li>
          <svg class="contact-icon" viewBox="0 0 16 16" aria-hidden="true">
            <circle cx="8" cy="8" r="8" fill="#c8372d"/>
            <circle cx="8" cy="8" r="4" fill="none" stroke="#fff" stroke-width="1"/>
            <path d="M4 8h8M8 4c-2 2.4-2 5.6 0 8M8 4c2 2.4 2 5.6 0 8" fill="none" stroke="#fff" stroke-width="0.8"/>
          </svg>
          www.Brivolaneute.com
        </li>
      </ul>
      <p class="division">A Division of Harmond Vistas, LLC</p>
    </div>
  </section>

  <section class="card card-back" aria-label="Card back">
    <div class="brand"><span class="brand-dot"></span>Brivo Lane Ute</div>
  </section>
</main>
</body>
</html>
```